Bref créative
Healthcare apparel brand
Business Card, Letter head, Envelope, Email stationary
I need double sided standard sized Business Card [3.5" x 2"]
Bank Gothic and complimenting fonts
Professional
Marcus Pellandrou
CEO / Founder
482 Folwell Lane Suite B217
Santa Barbara, CA 93184
marcusp@brightloomwovens.example
www.veltunic.example
the corporation is Bright Loom Wovens LLC. The brand is Vel Tunic. I want to prominently display the green cross. Large. Maybe watermark. slogan "Fabrics for Change"
"A highly technical base layer which permanently guards against degradation from micro-organisms." and either one of
"A better choice" or "Just what the doctor ordered"
Logo

```html
<!DOCTYPE html>
<html lang="en">
<head>
<meta charset="utf-8">
<title>Vel Tunic Stationery</title>
<link href="https://fonts.googleapis.com/css2?family=Michroma&family=Open+Sans:wght@400;600&display=swap" rel="stylesheet">
<style>
:root{
  --green:#7cc242;
  --green-dark:#5fa02e;
  --ink:#3b3b3b;
  --grey:#8a8a8a;
  --bg:#ececec;
  --paper:#ffffff;
  --card-dark:#4a4a4a;
  --line:#cfcfcf;
}
*{margin:0;padding:0;box-sizing:border-box}
html,body{width:1200px;height:643px;overflow:hidden;background:var(--bg)}
body{position:relative;font-family:"Open Sans",Arial,sans-serif;color:var(--ink)}
.sheet{position:absolute;background:var(--paper);box-shadow:0 1px 4px rgba(0,0,0,.18);overflow:hidden}
.brand{display:flex;align-items:center;justify-content:center;gap:6px}
.brand-mark{width:14px;height:14px;background:var(--green);flex:none}
.brand-name{font-family:"Michroma",sans-serif;color:var(--ink);font-size:15px;letter-spacing:1px;white-space:nowrap}
.slogan{font-family:"Michroma",sans-serif;font-size:4.5px;letter-spacing:2px;color:var(--grey);text-align:center;margin-top:2px}
.copy{font-size:4.6px;line-height:1.55;color:#555}
.copy p{margin-bottom:6px}
.footer{position:absolute;left:0;right:0;bottom:0}
.footer-grey{height:12px;background:#e2e2e2;font-size:4.4px;color:#666;display:flex;align-items:center;justify-content:center;gap:14px}
.footer-green{height:4px;background:var(--green)}
/* fax */
.fax{left:24px;top:24px;width:356px;height:606px}
.fax .head{padding-top:22px}
.fax-title{position:absolute;right:26px;top:112px;font-family:"Michroma",sans-serif;font-size:7px}
.fax-table{position:absolute;left:26px;top:122px;border-collapse:collapse;font-size:5px;width:304px}
.fax-table td{border:1px solid var(--line);height:11px;padding:0 3px}
.fax-table td.label{width:40px;color:#666}
.checks{position:absolute;left:26px;top:214px;display:flex;gap:16px;font-size:4.8px;color:#555}
.checks span::before{content:"";display:inline-block;width:5px;height:5px;border:1px solid #888;margin-right:3px;vertical-align:-1px}
.fax .copy{position:absolute;left:26px;right:26px;top:236px}
.sig{width:40px;height:10px;border-bottom:1px solid #999;margin:4px 0 3px}
.stamp{position:absolute;width:26px;height:26px;border-radius:50%;border:2px solid #9c96c8}
/* letterhead */
.letter{left:391px;top:24px;width:372px;height:606px}
.letter .head{padding-top:22px}
.letter .address{position:absolute;left:28px;top:100px;font-size:4.8px;line-height:1.5;color:#555}
.letter .copy{position:absolute;left:28px;right:28px;top:140px}
/* cards */
.card{position:absolute;width:195px;height:96px;box-shadow:0 1px 3px rgba(0,0,0,.2);overflow:hidden}
.card.light{background:var(--paper)}
.card.dark{background:var(--card-dark)}
.card.dark .brand-name{color:#fff}
.card .front{position:absolute;inset:0;display:flex;flex-direction:column;align-items:center;justify-content:center}
.card .band{position:absolute;left:0;right:0;bottom:0;height:5px;background:var(--green)}
.card .back{position:absolute;left:12px;right:12px;top:10px;display:flex;flex-direction:column;font-size:4.8px;line-height:1.55;color:#555}
.card.dark .back{color:#ddd}
.card .back .brand{justify-content:flex-start;gap:4px;margin-bottom:8px}
.card .back .brand-name{font-size:9px}
.card .back .brand-mark{width:9px;height:9px}
.card .back .who{font-family:"Michroma",sans-serif;font-size:6px;color:var(--ink);white-space:nowrap}
.card.dark .back .who{color:#fff}
.card .back .role{color:var(--green);margin-bottom:4px}
/* envelope */
.sheet2{left:785px;top:252px;width:401px;height:384px}
.sheet2 .brand{justify-content:flex-start;position:absolute;left:20px;top:22px}
.sheet2 .slogan{position:absolute;left:20px;top:42px;text-align:left}
.sheet2 .copy{position:absolute;left:20px;top:64px;width:180px}
.watermark{position:absolute;left:150px;top:200px;width:60px;height:60px;background:var(--green);opacity:.18}
</style>
</head>
<body>

<section class="sheet fax">
  <div class="head">
    <div class="brand"><span class="brand-mark"></span><span class="brand-name">VEL TUNIC</span></div>
    <div class="slogan">FABRICS FOR CHANGE</div>
  </div>
  <div class="fax-title">FAX</div>
  <table class="fax-table">
    <tr><td class="label">To:</td><td></td><td class="label">From:</td><td></td></tr>
    <tr><td class="label">Fax:</td><td></td><td class="label">Pages:</td><td></td></tr>
    <tr><td class="label">Phone:</td><td></td><td class="label">Date:</td><td></td></tr>
    <tr><td class="label">Re:</td><td></td><td class="label">CC:</td><td></td></tr>
    <tr><td class="label">Notes:</td><td colspan="3"></td></tr>
  </table>
  <div class="checks"><span>Urgent</span><span>For Review</span><span>Please Comment</span><span>Please Reply</span><span>Please Recycle</span></div>
  <div class="copy">
    <p>Dear Helena Varrow,</p>
    <p>Thank you for your continued interest in our healthcare apparel. Our team has prepared the requested samples and fabric notes for your review. Please let us know if you need further details on sizing, finishes or delivery times for your staff.</p>
    <p>Our base layer permanently guards against degradation from micro-organisms, keeping garments fresh through long shifts and repeated laundering. We would be glad to arrange a short call to walk you through the test results and care guidance.</p>
    <p>Please find the order summary attached. If any of the quantities need to change, reply to this fax or contact our office and we will update the schedule right away.</p>
    <p>Best regards,</p>
    <div class="sig"></div>
    <p>Marcus Pellandrou<br>CEO / Founder</p>
  </div>
  <div class="stamp" style="left:60px;bottom:34px"></div>
  <div class="footer">
    <div class="footer-grey"><span>482 Folwell Lane Suite B217, Santa Barbara, CA 93184</span><span>marcusp@brightloomwovens.example</span><span>www.veltunic.example</span></div>
    <div class="footer-green"></div>
  </div>
</section>

<section class="sheet letter">
  <div class="head">
    <div class="brand"><span class="brand-mark"></span><span class="brand-name">VEL TUNIC</span></div>
    <div class="slogan">FABRICS FOR CHANGE</div>
  </div>
  <div class="address">Helena Varrow<br>190 Larkspur Court<br>Ojai, CA 93023</div>
  <div class="copy">
    <p>Dear Helena Varrow,</p>
    <p>Thank you for your continued interest in our healthcare apparel. Our team has prepared the requested samples and fabric notes for your review. Please let us know if you need further details on sizing, finishes or delivery times for your staff and departments.</p>
    <p>A highly technical base layer which permanently guards against degradation from micro-organisms. Every garment is built to stay comfortable through long shifts, to hold its shape and colour after repeated laundering, and to give care teams one less thing to worry about.</p>
    <p>We would be glad to arrange a short call to walk you through the latest test results, the available colours and the care guidance for each fabric. Our samples can be shipped to your office within the week if that suits your planning.</p>
    <p>Please find the proposal attached. If any quantities or sizes need to change, reply to this letter or contact our office and we will update the schedule and pricing right away. We look forward to working with you.</p>
    <p>Best regards,</p>
    <div class="sig"></div>
    <p>Marcus Pellandrou<br>CEO / Founder, Bright Loom Wovens LLC</p>
  </div>
  <div class="stamp" style="left:70px;bottom:36px"></div>
  <div class="footer">
    <div class="footer-grey"><span>482 Folwell Lane Suite B217, Santa Barbara, CA 93184</span><span>marcusp@brightloomwovens.example</span><span>www.veltunic.example</span></div>
    <div class="footer-green"></div>
  </div>
</section>

<div class="card light" style="left:785px;top:24px">
  <div class="front">
    <div class="brand"><span class="brand-mark"></span><span class="brand-name">VEL TUNIC</span></div>
    <div class="slogan">FABRICS FOR CHANGE</div>
  </div>
  <div class="band"></div>
</div>
<div class="card light" style="left:991px;top:24px">
  <div class="back">
    <div class="brand"><span class="brand-mark"></span><span class="brand-name">VEL TUNIC</span></div>
    <div class="who">MARCUS PELLANDROU</div>
    <div class="role">CEO / Founder</div>
    <div>482 Folwell Lane Suite B217<br>Santa Barbara, CA 93184<br>marcusp@brightloomwovens.example<br>www.veltunic.example</div>
  </div>
  <div class="band"></div>
</div>

<div class="card dark" style="left:785px;top:132px">
  <div class="front">
    <div class="brand"><span class="brand-mark"></span><span class="brand-name">VEL TUNIC</span></div>
    <div class="slogan">FABRICS FOR CHANGE</div>
  </div>
  <div class="band"></div>
</div>
<div class="card dark" style="left:991px;top:132px">
  <div class="back">
    <div class="brand"><span class="brand-mark"></span><span class="brand-name">VEL TUNIC</span></div>
    <div class="who">MARCUS PELLANDROU</div>
    <div class="role">CEO / Founder</div>
    <div>482 Folwell Lane Suite B217<br>Santa Barbara, CA 93184<br>marcusp@brightloomwovens.example<br>www.veltunic.example</div>
  </div>
  <div class="band"></div>
</div>

<section class="sheet sheet2">
  <div class="brand"><span class="brand-mark"></span><span class="brand-name">VEL TUNIC</span></div>
  <div class="slogan">FABRICS FOR CHANGE</div>
  <div class="copy">Bright Loom Wovens LLC<br>482 Folwell Lane Suite B217<br>Santa Barbara, CA 93184</div>
  <div class="watermark"></div>
</section>

</body>
</html>
```